KMR Brochure

Brochure to communicate the concept and financial value of the company and its services to an executive audience. Attachments have detailed copy I want to use.
Updates

I have added a file that includes high res versions of company logo.

Reason: I am worried that the feedback and creation of new versions may take too long to complete by Sunday! This deadline will NOT move again though.

Target Market(s)

Chief Financial Officers in hospitals and other health organizations

Industry/Entity Type

Financial

Requirements
Must have
• Must be a 2-sided, single page.

```html
<!DOCTYPE html>
<html lang="en">
<head>
<meta charset="utf-8">
<title>KMR – Solutions for a Stronger Bottom Line</title>
<link href="https://fonts.googleapis.com/css2?family=Open+Sans:ital,wght@0,400;0,600;0,700;1,700&display=swap" rel="stylesheet">
<style>
  :root {
    --brand-blue: #1b7bc0;
    --text-dark: #2b2b2b;
    --text-body: #3a3a3a;
    --frame-green: #8db43e;
    --bullet-green: #8db43e;
    --logo-grey: #4a4a4a;
    --page-bg: #ffffff;
  }
  * { margin: 0; padding: 0; box-sizing: border-box; }
  html, body { width: 927px; height: 1200px; overflow: hidden; background: var(--page-bg); }
  body { font-family: "Open Sans", Arial, sans-serif; color: var(--text-body); }
  .page { position: relative; width: 927px; height: 1200px; }

  .headline {
    position: absolute; left: 55px; top: 108px;
    font-size: 25px; font-weight: 400; color: var(--brand-blue); letter-spacing: -0.2px;
  }

  .brand {
    position: absolute; left: 660px; top: 60px;
    display: flex; align-items: center; gap: 14px;
  }
  .brand-mark { width: 14px; height: 14px; background: var(--brand-blue); }
  .brand-name {
    border-left: 1px solid #9a9a9a; padding-left: 10px;
    font-size: 21px; line-height: 26px; font-weight: 700; color: var(--logo-grey);
    text-transform: uppercase; letter-spacing: 0.3px;
  }

  .service { position: absolute; left: 55px; width: 800px; display: flex; gap: 22px; }
  .service-photo {
    flex: 0 0 170px; height: 165px; border: 1px solid var(--frame-green);
  }
  .photo-keypad { background: linear-gradient(135deg, #3a3a3a 0%, #111 45%, #6b5a4a 75%, #1b1b1b 100%); }
  .photo-building { background: linear-gradient(160deg, #4f7fc0 0%, #9fbfe4 35%, #c9b79a 60%, #7b6e5c 100%); }
  .photo-surgery { background: linear-gradient(135deg, #4f8e95 0%, #8fb9b8 40%, #2f5f6b 75%, #d7c3a3 100%); }
  .photo-finance { background: linear-gradient(135deg, #d39a4e 0%, #f0cf96 40%, #b97a36 75%, #e9c488 100%); }

  .service-text { padding-top: 2px; }
  .service-title { font-size: 17.5px; font-weight: 600; color: var(--brand-blue); margin-bottom: 9px; }
  .service-lead { font-size: 14.5px; font-weight: 700; font-style: italic; color: var(--text-dark); line-height: 24px; margin-bottom: 8px; }
  .service-body { font-size: 14px; line-height: 24.5px; }
  .service-body + .service-body { margin-top: 12px; }
  .service-body strong { font-weight: 700; color: var(--text-dark); }

  .footer {
    position: absolute; left: 57px; top: 1128px;
    font-size: 13.5px; color: var(--text-body); display: flex; align-items: center; gap: 9px;
  }
  .footer-dot { width: 5px; height: 5px; border-radius: 50%; background: var(--bullet-green); }
</style>
</head>
<body>
<div class="page">
  <h1 class="headline">Solutions for a Stronger Bottom Line</h1>

  <div class="brand">
    <span class="brand-mark"></span>
    <div class="brand-name">The<br>Clinical<br>Value<br>Alliance</div>
  </div>

  <section class="service" style="top:224px">
    <div class="service-photo photo-keypad" role="img" aria-label="Close-up of a finger pressing calculator keys"></div>
    <div class="service-text">
      <h2 class="service-title">Strategic Sourcing</h2>
      <p class="service-lead">Supplier spending often comprises 35-40% of a hospital’s operating costs.<br>This is a significant cost reduction opportunity.</p>
      <p class="service-body">Using deep subject matter expertise and a large real time database, our sourcing efforts deliver an average savings of 18%. Our team has worked with over 500 clients since 1992, with experience in over 100 spend categories. We consistently exceed GPO savings.</p>
    </div>
  </section>

  <section class="service" style="top:424px">
    <div class="service-photo photo-building" role="img" aria-label="Tall hospital building against a blue sky"></div>
    <div class="service-text">
      <h2 class="service-title">Energy Conservation</h2>
      <p class="service-lead">Hospitals are among the largest users of energy per sq. ft. EPA estimates that<br>an average of 30% of energy consumed by commercial buildings is wasted.</p>
      <p class="service-body">Our engineers evaluate your facility’s mechanical systems, controls, and energy usage,<br>identifying and implementing non-capital projects that reduce consumption and costs<br>by 10-30%.</p>
    </div>
  </section>

  <section class="service" style="top:621px">
    <div class="service-photo photo-surgery" role="img" aria-label="Surgical team working in an operating room"></div>
    <div class="service-text">
      <h2 class="service-title">Surgical Staffing</h2>
      <p class="service-lead">Facilities often provide surgical first assistance without reimbursement.<br>Surgeons often ask colleagues to assist in cases.</p>
      <p class="service-body">Our “in-sourcing” program provides trained professional surgical first assistants (SFA’s) to hospitals and surgery centers to offset expenses, increase throughput, and provide the best possible support for surgeons and their patients.</p>
    </div>
  </section>

  <section class="service" style="top:819px">
    <div class="service-photo photo-finance" role="img" aria-label="Reading glasses resting on a printed financial table"></div>
    <div class="service-text">
      <h2 class="service-title">Revenue Analytics</h2>
      <p class="service-lead">Few hospitals realize the full potential of the data they collect every day.</p>
      <p class="service-body"><strong>Pricing.</strong> Mathematically implemented strategic pricing, optimization of price sensitive<br>net revenue based on market position, patient mix, contracts, and your business rules.</p>
      <p class="service-body"><strong>Charge Capture.</strong> Analysis of charge data vs. a repository of standards. Analysis of completeness of claims to identify and realize revenue gains.</p>
      <p class="service-body"><strong>ICD-10.</strong> Analytics to identify areas of high vs. low risk and complexity, enabling better prioritization of efforts.</p>
    </div>
  </section>

  <footer class="footer">
    <span>www.ClinicalValueAlliance.com</span><span class="footer-dot"></span>
    <span>info@kmrpartners.net</span><span class="footer-dot"></span>
    <span>(206) 555-0147</span><span class="footer-dot"></span>
    <span>Copyright 2013 KMR Partners LLC</span>
  </footer>
</div>
</body>
</html>
```